"Mirren Hatch" Mobile 2D Game

We need a mobile design for the main screen of the game (with a popup design to select the ball color), for a Professional IT Team. Our initial game is "Mirren Hatch", classic board game for kids and even non kids. We would like to see design that suitable for mobile devices (small and tablet). The main concept of the game will be something similar to this video link: https://www.vidstorn.com/watch?v=QtR8kLmzPwe

Please be sure the balls inside the game board have readable numbers. Thanks!

Requirements
Must have
• Separate layers for each UI component so it can be exported easily

```html
<!DOCTYPE html>
<html lang="en">
<head>
<meta charset="utf-8">
<title>Mirren Hatch – Main Screen</title>
<link href="https://fonts.googleapis.com/css2?family=Luckiest+Guy&display=swap" rel="stylesheet">
<style>
  :root{
    --bg:#e6e6e6;
    --ink:#011523;
    --blue:#0ca0c3;
    --pink:#f799ef;
    --tile:#878787;
    --line:#555555;
    --arrow:#6ebd45;
    --white:#ffffff;
    --c-green:#035e48;
    --c-purple:#4c0a55;
    --c-red:#ae0023;
    --c-rust:#b83200;
    --c-orange:#ec851f;
    --c-yellow:#ecc51a;
  }
  html,body{margin:0;padding:0;overflow:hidden;background:var(--bg);}
  .screen{width:675px;height:1200px;overflow:hidden;background:var(--bg);}
  .screen svg{display:block;width:675px;height:1200px;}
  text{font-family:"Luckiest Guy",cursive;text-anchor:middle;dominant-baseline:central;}
  .game-title{fill:var(--ink);font-size:86px;}
  .title-dot{fill:var(--blue);}
  .ball-blue{fill:var(--blue);}
  .ball-pink{fill:var(--pink);}
  .ball-label{fill:var(--white);font-size:46px;}
  .grid-line{stroke:var(--line);stroke-width:4;}
  .tile{fill:var(--tile);}
  .arrow{fill:var(--arrow);}
  .cell-points{fill:var(--blue);font-size:54px;}
  .popup-frame{fill:var(--white);}
  .popup-body{fill:var(--bg);}
  .popup-title{fill:var(--blue);font-size:76px;}
  .play-icon{fill:var(--white);}
  .score-label{fill:var(--ink);font-size:84px;}
  .score-value{fill:var(--white);font-size:86px;}
</style>
</head>
<body>
<main class="screen">
<svg viewBox="0 0 1080 1920" xmlns="http://www.w3.org/2000/svg">
  <!-- header -->
  <g class="header">
    <circle class="title-dot" cx="210" cy="76" r="26"/>
    <text class="game-title" x="560" y="80">Mirren Hatch</text>
  </g>

  <!-- queued balls -->
  <g class="ball-queue">
    <circle class="ball-blue" cx="97" cy="183" r="48"/><text class="ball-label" x="97" y="186">95</text>
    <circle class="ball-pink" cx="318" cy="183" r="48"/><text class="ball-label" x="318" y="186">30</text>
    <circle class="ball-blue" cx="540" cy="183" r="48"/><text class="ball-label" x="540" y="186">75</text>
    <circle class="ball-blue" cx="649" cy="183" r="48"/><text class="ball-label" x="649" y="186">15</text>
    <circle class="ball-blue" cx="761" cy="183" r="48"/><text class="ball-label" x="761" y="186" style="font-size:40px">120</text>
    <circle class="ball-pink" cx="870" cy="183" r="48"/><text class="ball-label" x="870" y="186">5</text>
    <circle class="ball-blue" cx="985" cy="183" r="48"/><text class="ball-label" x="985" y="186">40</text>
  </g>

  <!-- board tiles -->
  <g class="board-tiles">
    <rect class="tile" x="374" y="237" width="110" height="107"/>
    <rect class="tile" x="485" y="345" width="110" height="110"/>
    <rect class="tile" x="818" y="345" width="110" height="110"/>
    <rect class="tile" x="153" y="456" width="110" height="110"/>
    <rect class="tile" x="929" y="456" width="106" height="110"/>
    <rect class="tile" x="818" y="567" width="110" height="110"/>
    <rect class="tile" x="929" y="567" width="106" height="110"/>
    <rect class="tile" x="153" y="1010" width="110" height="110"/>
    <rect class="tile" x="264" y="1232" width="110" height="110"/>
    <rect class="tile" x="707" y="1232" width="110" height="110"/>
    <rect class="tile" x="264" y="1342" width="110" height="110"/>
    <rect class="tile" x="707" y="1453" width="110" height="110"/>
    <rect class="tile" x="929" y="1453" width="106" height="110"/>
    <rect class="tile" x="43" y="1564" width="108" height="106"/>
    <rect class="tile" x="707" y="1564" width="110" height="106"/>
  </g>

  <!-- grid lines -->
  <g class="board-grid">
    <line class="grid-line" x1="152" y1="237" x2="152" y2="1670"/>
    <line class="grid-line" x1="263" y1="237" x2="263" y2="1670"/>
    <line class="grid-line" x1="373" y1="237" x2="373" y2="1670"/>
    <line class="grid-line" x1="484" y1="237" x2="484" y2="1670"/>
    <line class="grid-line" x1="595" y1="237" x2="595" y2="1670"/>
    <line class="grid-line" x1="706" y1="237" x2="706" y2="1670"/>
    <line class="grid-line" x1="817" y1="237" x2="817" y2="1670"/>
    <line class="grid-line" x1="928" y1="237" x2="928" y2="1670"/>
    <line class="grid-line" x1="43" y1="344" x2="1035" y2="344"/>
    <line class="grid-line" x1="43" y1="455" x2="1035" y2="455"/>
    <line class="grid-line" x1="43" y1="566" x2="1035" y2="566"/>
    <line class="grid-line" x1="43" y1="677" x2="1035" y2="677"/>
    <line class="grid-line" x1="43" y1="788" x2="1035" y2="788"/>
    <line class="grid-line" x1="43" y1="899" x2="1035" y2="899"/>
    <line class="grid-line" x1="43" y1="1009" x2="1035" y2="1009"/>
    <line class="grid-line" x1="43" y1="1120" x2="1035" y2="1120"/>
    <line class="grid-line" x1="43" y1="1231" x2="1035" y2="1231"/>
    <line class="grid-line" x1="43" y1="1341" x2="1035" y2="1341"/>
    <line class="grid-line" x1="43" y1="1452" x2="1035" y2="1452"/>
    <line class="grid-line" x1="43" y1="1563" x2="1035" y2="1563"/>
  </g>

  <!-- direction arrows -->
  <g class="board-arrows">
    <polygon class="arrow" points="402,258 402,321 457,290"/>
    <polygon class="arrow" points="228,477 228,540 173,509"/>
    <polygon class="arrow" points="960,477 960,540 1015,509"/>
    <polygon class="arrow" points="904,588 904,651 850,620"/>
    <polygon class="arrow" points="1011,588 1011,651 957,620"/>
    <polygon class="arrow" points="293,1252 293,1315 348,1284"/>
    <polygon class="arrow" points="734,1252 734,1315 790,1284"/>
    <polygon class="arrow" points="73,1585 73,1645 128,1615"/>
    <polygon class="arrow" points="734,1585 734,1648 790,1617"/>
  </g>

  <!-- cell points & board balls -->
  <g class="board-points">
    <text class="cell-points" x="761" y="398">10</text>
    <text class="cell-points" x="872" y="1289">50</text>
    <text class="cell-points" x="207" y="1399">25</text>
    <circle class="ball-blue" cx="96" cy="1508" r="48"/>
    <text class="ball-label" x="96" y="1511">5</text>
  </g>

  <!-- colour picker popup -->
  <g class="color-popup">
    <rect class="popup-frame" x="247" y="563" width="604" height="603"/>
    <rect class="popup-body" x="263" y="578" width="573" height="572"/>
    <text class="popup-title" x="550" y="684">Select the</text>
    <text class="popup-title" x="550" y="790">Ball Color</text>
    <g class="color-options">
      <circle cx="373" cy="924" r="48" fill="var(--c-green)"/>
      <circle cx="490" cy="924" r="48" fill="var(--blue)"/>
      <polygon class="play-icon" points="467,894 467,956 527,925"/>
      <circle cx="608" cy="924" r="48" fill="var(--c-purple)"/>
      <circle cx="725" cy="924" r="48" fill="var(--c-red)"/>
      <circle cx="373" cy="1049" r="48" fill="var(--pink)"/>
      <circle cx="490" cy="1049" r="48" fill="var(--c-rust)"/>
      <circle cx="608" cy="1049" r="48" fill="var(--c-orange)"/>
      <circle cx="725" cy="1049" r="48" fill="var(--c-yellow)"/>
    </g>
  </g>

  <!-- score bar -->
  <g class="score-bar">
    <circle class="ball-blue" cx="262" cy="1789" r="97"/>
    <text class="score-value" x="262" y="1793">250</text>
    <text class="score-label" x="541" y="1797">Score</text>
    <circle class="ball-pink" cx="820" cy="1789" r="97"/>
    <text class="score-value" x="820" y="1793">750</text>
  </g>
</svg>
</main>
</body>
</html>
```